Business cards for law firm with global theme

I'd like business cards with contact info for two offices. They should include the colors and font of the new logo design, which is a stylized globe with an "F" in it. The feel should be very modern and professional.

```html
<!DOCTYPE html>
<html lang="en">
<head>
<meta charset="UTF-8">
<title>Whitcombe Law – Business Cards</title>
<link rel="stylesheet" href="https://fonts.googleapis.com/css2?family=Open+Sans:wght@400;600;700;800&display=swap">
<style>
  :root {
    --page-bg: #e9e7e3;
    --navy-deep: #161a45;
    --navy: #262b62;
    --navy-glow: #3b3f7a;
    --ocean: #1f4f7e;
    --sky: #2fa9e1;
    --white: #ffffff;
    --band: #e6e7ea;
    --band-text: #262b62;
  }
  * { box-sizing: border-box; margin: 0; padding: 0; }
  html, body {
    width: 1200px; height: 960px; overflow: hidden;
    background: var(--page-bg);
    font-family: "Open Sans", Arial, sans-serif;
  }
  .stage {
    width: 1200px; height: 960px;
    display: flex; flex-direction: column; align-items: center; justify-content: center;
    gap: 44px;
  }
  .card {
    position: relative;
    width: 660px; height: 378px;
    overflow: hidden;
    box-shadow: 0 10px 28px rgba(20, 20, 40, 0.25);
  }

  /* ---------- Back ---------- */
  .card-back {
    background:
      radial-gradient(ellipse 70% 90% at 62% 40%, var(--ocean) 0%, #1b3a6a 45%, transparent 80%),
      linear-gradient(135deg, var(--navy) 0%, var(--navy-deep) 100%);
  }
  .card-back .brand {
    position: absolute; right: 70px; top: 150px;
  }
  .brand {
    display: flex; align-items: center; gap: 14px;
  }
  .brand-dot {
    width: 54px; height: 54px; border-radius: 50%;
    background: var(--sky);
    flex: none;
  }
  .brand-name {
    color: var(--white);
    font-weight: 800;
    font-size: 34px;
    letter-spacing: 1px;
    white-space: nowrap;
  }

  /* ---------- Front ---------- */
  .card-front {
    background: radial-gradient(ellipse 75% 85% at 40% 30%, var(--navy-glow) 0%, var(--navy) 45%, var(--navy-deep) 100%);
  }
  .card-front .brand {
    position: absolute; left: 250px; top: 54px;
  }
  .card-front .brand-dot { width: 64px; height: 64px; }
  .card-front .brand-name { font-size: 34px; }

  .holder {
    position: absolute; right: 402px; top: 156px;
    text-align: right; color: var(--white);
  }
  .holder-name {
    font-weight: 700; font-size: 19px; letter-spacing: 0.5px;
  }
  .holder-role {
    font-weight: 400; font-size: 16px; margin-top: 2px;
  }
  .divider {
    position: absolute; left: 274px; top: 150px;
    width: 1px; height: 104px; background: rgba(255,255,255,0.75);
  }
  .contacts {
    position: absolute; left: 298px; top: 158px;
    list-style: none; color: var(--white);
    font-size: 16px; line-height: 30px;
  }
  .contacts li { display: flex; align-items: center; gap: 10px; }
  .contacts svg { width: 18px; height: 18px; flex: none; }
  .contacts .accent { color: var(--sky); font-weight: 600; }

  .offices-band {
    position: absolute; left: 0; bottom: 22px;
    width: 100%; height: 52px;
    background: var(--band);
    display: flex; align-items: center;
    padding-left: 150px;
    color: var(--band-text);
    font-size: 16px;
  }
  .edge-strip {
    position: absolute; left: 0; bottom: 0;
    width: 100%; height: 22px; background: var(--navy);
  }
</style>
</head>
<body>
<main class="stage">

  <section class="card card-back" aria-label="Card back">
    <div class="brand">
      <span class="brand-dot"></span>
      <span class="brand-name">WHITCOMBE LAW</span>
    </div>
  </section>

  <section class="card card-front" aria-label="Card front">
    <div class="brand">
      <span class="brand-dot"></span>
      <span class="brand-name">WHITCOMBE LAW</span>
    </div>

    <div class="holder">
      <p class="holder-name">DANA R. WHITCOMBE</p>
      <p class="holder-role">Attorney at law</p>
    </div>

    <div class="divider"></div>

    <ul class="contacts">
      <li>
        <svg viewBox="0 0 24 24" aria-hidden="true"><path fill="#2fa9e1" d="M6.6 10.8a15.1 15.1 0 0 0 6.6 6.6l2.2-2.2c.3-.3.7-.4 1-.2 1.1.4 2.3.6 3.6.6.6 0 1 .4 1 1V20c0 .6-.4 1-1 1A17 17 0 0 1 3 4c0-.6.4-1 1-1h3.5c.6 0 1 .4 1 1 0 1.3.2 2.5.6 3.6.1.3 0 .7-.2 1z"/></svg>
        <span>(555) 014-2290</span>
      </li>
      <li>
        <svg viewBox="0 0 24 24" aria-hidden="true"><rect x="2" y="5" width="20" height="14" rx="1" fill="#2fa9e1"/><path d="M2.5 5.5 12 13l9.5-7.5" fill="none" stroke="#262b62" stroke-width="1.6"/></svg>
        <span>info@whitcombelaw.com</span>
      </li>
      <li>
        <svg viewBox="0 0 24 24" aria-hidden="true"><circle cx="12" cy="12" r="9.5" fill="none" stroke="#2fa9e1" stroke-width="2"/><ellipse cx="12" cy="12" rx="4" ry="9.5" fill="none" stroke="#2fa9e1" stroke-width="1.6"/><path d="M2.5 12h19M4 7h16M4 17h16" stroke="#2fa9e1" stroke-width="1.4"/></svg>
        <span>www.<span class="accent">whitcombelaw</span>.com</span>
      </li>
    </ul>

    <div class="offices-band">New York &amp; Washington D.C.</div>
    <div class="edge-strip"></div>
  </section>

</main>
</body>
</html>
```